Flyer Design Project for high quality paving products for landscaping

Brellow paving stones is a long established manufacturer and supplier of concrete paving, pool coping and landscape features.
it is known as a premium, top end product which over recent years has lost market share to imported natural stone which is in some cases a lot cheaper. There is a perception that natural stone is better and now also cheaper.

I think a lot of the information required for the flyer is already on our web site www.brellow.com.au We service the following types of customers; Architects, Pool Builders, Landscape designers, Landscape contractors and private customers. A lot of times our product is specified by a designer and then the private customer comes to our showroom for final selection. The main purpose of this flyer would to give to the private customer when they come to us for final selection, reinforcing the value of our brand and product.

Target Market(s)

Middle to upper class who have paid for a designer. Like our product but cant help being drawn to a cheaper alternative.

Industry/Entity Type

Landscaping

Requirements
Must have
• Must use existing Brellow logo.
Nice to have
• We have one awards. Gold medals. Landscaping is very visual. Images as well as inspirational text. Not to technical.

I think of Brellow as Valtore. THey have Sports cars, Luxury cars, Commercial vehicles, family cars. Wide customer base but always with valtore branding and quality.
Should not have
• Want to let people know we can supply products that are affordable if they have a budget without compromising our brand as atop end product.

```html
<!DOCTYPE html>
<html lang="en">
<head>
<meta charset="utf-8">
<title>Brellow Paving Stones – Trifold Flyer</title>
<link rel="stylesheet" href="https://fonts.googleapis.com/css2?family=Josefin+Sans:wght@300;400;600&display=swap">
<style>
  :root {
    --page-bg: #ececec;
    --panel-dark: #2b2b2d;
    --panel-darker: #1b1b1d;
    --bar-grey: #6b6d72;
    --bar-grey-light: #8e9096;
    --text-light: #f2f2f2;
    --text-soft: #c9c9cc;
    --stripe: #d9d9dc;
    --pool-blue: #6fb6cf;
    --pool-deep: #2f6f8c;
    --dusk-sky: #6f8fb8;
    --warm-light: #d9b47a;
  }
  * { margin: 0; padding: 0; box-sizing: border-box; }
  html, body { width: 1200px; height: 905px; overflow: hidden; }
  body {
    background: var(--page-bg);
    font-family: "Josefin Sans", sans-serif;
    color: var(--text-light);
  }
  .flyer {
    position: absolute;
    left: 90px; top: 92px;
    width: 1020px; height: 720px;
    display: flex;
    box-shadow: 0 12px 30px rgba(0,0,0,0.25);
  }
  .panel {
    position: relative;
    width: 340px; height: 720px;
    overflow: hidden;
    background: linear-gradient(180deg, var(--panel-dark), var(--panel-darker));
  }

  /* shared brand name */
  .brand-name {
    font-family: "Josefin Sans", sans-serif;
    font-weight: 400;
    color: var(--text-light);
    letter-spacing: 0.18em;
    text-transform: uppercase;
    line-height: 1.1;
  }
  .brand-name .line-1 { display: block; font-size: 26px; }
  .brand-name .line-2 { display: block; font-size: 11px; letter-spacing: 0.32em; margin-top: 4px; }

  /* inside panel */
  .panel-inside { padding: 34px 24px 0 28px; }
  .panel-inside .brand-name { margin-bottom: 22px; }
  .section-bar {
    display: block;
    width: 250px;
    padding: 7px 14px 5px;
    margin: 12px 0 10px -6px;
    background: linear-gradient(90deg, var(--bar-grey), var(--bar-grey-light) 70%, transparent);
    font-size: 19px;
    font-weight: 300;
    letter-spacing: 0.03em;
    text-transform: lowercase;
  }
  .section-copy {
    font-size: 11px;
    font-weight: 300;
    line-height: 1.55;
    color: var(--text-soft);
    padding-right: 6px;
  }
  .product-range { list-style: none; margin-top: 8px; }
  .product-range li {
    display: flex; align-items: center; gap: 14px;
    height: 34px;
    font-size: 10.5px; font-weight: 400;
  }
  .product-swatch {
    width: 70px; height: 28px;
    background: linear-gradient(135deg, #8a8a8c, #4a4a4c);
  }
  .feature-photo {
    position: absolute; left: 28px; right: 24px; bottom: 30px;
    height: 110px;
    background: linear-gradient(180deg, #3d3a33, #7a6a4c 55%, #2c2c2e);
    display: flex; align-items: flex-end; padding: 10px;
  }
  .feature-caption {
    font-size: 15px; font-weight: 600; letter-spacing: 0.08em;
    color: var(--warm-light); text-transform: uppercase; line-height: 1.1;
  }

  /* divider stripe */
  .fold-stripe { position: absolute; top: 0; left: 0; width: 340px; height: 720px; pointer-events: none; }

  /* middle panel */
  .panel-middle .brand-name { position: absolute; top: 34px; left: 30px; }
  .evening-photo {
    position: absolute; left: 0; right: 0; bottom: 0; height: 470px;
    clip-path: polygon(0 0, 100% 6%, 100% 100%, 0 100%);
    background: linear-gradient(180deg, var(--dusk-sky) 0%, #3f5470 28%, #a37a4a 48%, var(--pool-blue) 66%, var(--pool-deep) 100%);
  }
  .contact {
    position: absolute; left: 26px; bottom: 40px; width: 230px;
    font-size: 11px; font-weight: 300; line-height: 1.5; color: var(--text-light);
  }
  .contact h2 { font-size: 18px; font-weight: 300; text-transform: lowercase; margin-bottom: 6px; }

  /* cover panel */
  .panel-cover .cover-band { height: 150px; background: linear-gradient(180deg, #2e2e30, #202022); }
  .garden-photo {
    position: absolute; left: 0; right: 0; top: 150px; bottom: 0;
    background: linear-gradient(180deg, #3f5f93 0%, #5a7aa8 22%, #4d6a3a 40%, #c9c2ae 58%, var(--pool-blue) 74%, var(--pool-deep) 100%);
  }
  .panel-cover .brand-name { position: absolute; left: 0; right: 0; bottom: 70px; text-align: center; }
  .panel-cover .brand-name .line-1 { font-size: 40px; }
  .panel-cover .brand-name .line-2 { font-size: 15px; }
</style>
</head>
<body>
  <main class="flyer">
    <section class="panel panel-inside">
      <div class="brand-name"><span class="line-1">Brellow</span><span class="line-2">Paving Stones</span></div>

      <h2 class="section-bar">pool coping</h2>
      <p class="section-copy">Brellow range of pool coping is extensive and offers coping options for both concrete and fibreglass pools. We can also custom cut to suit curves, step edges and retrofit to existing pools.</p>

      <h2 class="section-bar">residential</h2>
      <p class="section-copy">Our quality, versatility, style and durability in combination with our customer service make Brellow Paving Stones the premier choice for residential landscaping.</p>

      <h2 class="section-bar">our product range</h2>
      <ul class="product-range">
        <li><span class="product-swatch" role="img" aria-label="Paving slab sample"></span>our paving range</li>
        <li><span class="product-swatch" role="img" aria-label="Streetscape paver sample"></span>streetscape paving</li>
        <li><span class="product-swatch" role="img" aria-label="Pool coping sample"></span>pool coping</li>
        <li><span class="product-swatch" role="img" aria-label="Step and sill sample"></span>steps/sills</li>
        <li><span class="product-swatch" role="img" aria-label="Landscape feature sample"></span>landscape features</li>
      </ul>

      <div class="feature-photo" role="img" aria-label="Evening photograph of a paved garden with stone bench and lighting">
        <span class="feature-caption">Award winning<br>paving stone</span>
      </div>

      <svg class="fold-stripe" viewBox="0 0 340 720" aria-hidden="true">
        <polygon points="300,0 318,0 340,170 340,215" fill="var(--stripe)" opacity="0.85"/>
      </svg>
    </section>

    <section class="panel panel-middle">
      <div class="brand-name"><span class="line-1">Brellow</span><span class="line-2">Paving Stones</span></div>
      <div class="evening-photo" role="img" aria-label="Dusk photograph of a modern home with lit interior, lawn and paved pool surround"></div>
      <div class="contact">
        <h2>contact us</h2>
        <p>Brellow Paving Stones<br>14 Harlow Street<br>Kelsworth VIC 3150<br>telephone 1300 555 014</p>
      </div>
    </section>

    <section class="panel panel-cover">
      <div class="cover-band"></div>
      <div class="garden-photo" role="img" aria-label="Night photograph of a pool with stone coping beside a green living wall and rendered pillar"></div>
      <div class="brand-name"><span class="line-1">Brellow</span><span class="line-2">Paving Stones</span></div>
    </section>
  </main>
</body>
</html>
```